Express envelope design for courier company

We're a courier company launching a new service for sending documents around Australia. We need a design for the express envelope that will be used to hold the documents during transit. The envelope will be printed in colour on cardboard. Please see brief attached.

Design cues:
• Vibrant
• Simplified
• Clean
• Aesthetically pleasing
• Artistic
• Nothing “institutional” or “Halvern Lines”
• Nothing cramped, no small text

It's fine to crop, recolour, or reinterpret the logo.

Industry/Entity Type

It Company

Font styles to use
Sans Serif

Requirements
Must have
• Dimensions:
• Back side: 350 x 230 mm
• Front side: 387.5 x 230 mm (including flap to close envelope)
• Back side barcode panel: 90 x 75 mm (blank area for adhesive barcode)
• Back side address panel: 150 x 90 mm (see PDF for contents and layout)
• Front side text:
• RM-ZO
• Express Envelope
• Send With Trust
• 1300 486 917
• rmzo-post.com.au
• Back side text:
• For documents
• Max. weight 500g, max width 20mm
• Send With Trust
• • Time-guaranteed and next-flight-out service for vital deliveries
• • Same-day and next-day local services
• • Overnight service to most Australian locations
• • Budget road service Australia-wide
• • Worldwide express courier
• Visit rmzo-post.com.au or phone 1300 486 917
• Flap text:
• Go to rmzo-post.com.au to book your pickup.
• Carried subject to RM-ZO Standard Conditions of Carriage; see our website.
Nice to have
• Our web colours:
• #fcd614
• #d06517
• #3b5274
• #f0f0d8
• #382a3a

```html
<!DOCTYPE html>
<html lang="en">
<head>
<meta charset="utf-8">
<title>RM-ZO Express Envelope</title>
<link rel="stylesheet" href="https://fonts.googleapis.com/css2?family=Barlow:wght@400;500;600;700&display=swap">
<style>
  :root {
    --backdrop: #eef0ee;
    --cream: #eff7d4;
    --orange: #d34a0a;
    --peach: #e3a06d;
    --blue: #244894;
    --yellow: #f8de0a;
    --flap: #231f20;
    --ink: #111111;
    --white: #ffffff;
  }
  html, body {
    margin: 0;
    padding: 0;
    width: 939px;
    height: 1200px;
    overflow: hidden;
    background: var(--backdrop);
  }
  .sheet {
    display: block;
    width: 939px;
    height: 1200px;
    font-family: "Barlow", sans-serif;
  }
  .flap { fill: var(--flap); }
  .flap-text { fill: var(--white); font-size: 10px; font-weight: 500; text-anchor: middle; }
  .body-panel { fill: var(--cream); }
  .field-orange { fill: var(--orange); }
  .field-blue { fill: var(--blue); }
  .field-yellow { fill: var(--yellow); }
  .globe-area { fill: var(--peach); }
  .brand-name { fill: var(--white); font-weight: 700; font-size: 60px; letter-spacing: 1px; }
  .headline { fill: var(--orange); font-weight: 700; font-size: 34px; text-anchor: end; letter-spacing: 0.5px; }
  .tagline { fill: var(--blue); font-weight: 500; font-size: 18px; text-anchor: end; }
  .contact { fill: var(--white); font-weight: 500; font-size: 18px; text-anchor: middle; }
  .doc-title { fill: var(--blue); font-weight: 700; font-size: 33px; }
  .doc-limits { fill: var(--orange); font-weight: 500; font-size: 17px; }
  .service-list { fill: var(--ink); font-weight: 500; font-size: 10.5px; }
  .address-box { fill: var(--cream); stroke: var(--orange); stroke-width: 0.8; }
  .address-rule { stroke: var(--orange); stroke-width: 0.8; }
  .address-label { fill: var(--orange); font-weight: 500; font-size: 10px; }
</style>
</head>
<body>
<svg class="sheet" viewBox="0 0 1000 1278" xmlns="http://www.w3.org/2000/svg">

  <!-- Front side of the envelope -->
  <g class="envelope-front">
    <rect class="body-panel" x="180" y="231" width="646" height="349"/>
    <polygon class="field-orange" points="330,231 826,231 826,580 660,580 475,388"/>
    <polygon class="field-blue" points="186,580 475,388 660,580"/>
    <rect class="globe-area" x="575" y="272" width="195" height="212" rx="90" opacity="0.85"
          role="img" aria-label="Globe illustration showing Australia and Asia"/>
    <text class="brand-name" x="572" y="397">RM-ZO</text>

    <text class="headline" x="383" y="356">EXPRESS</text>
    <text class="headline" x="383" y="396">ENVELOPE</text>
    <text class="tagline" x="386" y="419">Ship With Trust</text>
    <text class="contact" x="455" y="554">1300 486 917 | rmzo-post.com.au</text>

    <polygon class="flap" points="180,162 828,162 815,231 192,231"/>
    <text class="flap-text" x="510" y="191">Go to rmzo-post.com.au to book your pickup.</text>
    <text class="flap-text" x="510" y="207">Carried subject to RM-ZO Standard Conditions of Carriage; see our website.</text>
  </g>

  <!-- Back side of the envelope -->
  <g class="envelope-back">
    <rect class="body-panel" x="184" y="673" width="640" height="420"/>
    <polygon class="field-orange" points="824,673 824,1093 655,1093 472,905"/>
    <polygon class="field-yellow" points="184,1093 472,905 655,1093"/>
    <rect class="globe-area" x="600" y="756" width="160" height="128" rx="60" opacity="0.85"
          role="img" aria-label="Globe illustration showing Australia and Asia"/>
    <text class="brand-name" x="616" y="866" style="font-size:54px">RM-ZO</text>

    <text class="doc-title" x="216" y="738">For documents</text>
    <text class="doc-limits" x="216" y="764">Max. weight 500g, max width 20mm</text>
    <g class="service-list">
      <text x="215" y="797">SHIP WITH TRUST</text>
      <text x="215" y="812">• Time-guaranteed and next-flight-out service for vital deliveries</text>
      <text x="215" y="828">• Same-day and next-day local services</text>
      <text x="215" y="843">• Overnight service to most Australian locations</text>
      <text x="215" y="859">• Budget road service Australia-wide</text>
      <text x="215" y="874">• Worldwide express courier</text>
      <text x="215" y="890">Visit rmzo-post.com.au or phone 1300 486 917</text>
    </g>

    <g class="address-panel">
      <rect class="address-box" x="512" y="885" width="280" height="191"/>
      <line class="address-rule" x1="512" y1="921" x2="792" y2="921"/>
      <line class="address-rule" x1="512" y1="1045" x2="792" y2="1045"/>
      <line class="address-rule" x1="666" y1="1045" x2="666" y2="1076"/>
      <text class="address-label" x="524" y="906">Sender's name</text>
      <text class="address-label" x="524" y="945">Receiver</text>
      <text class="address-label" x="524" y="1061">State</text>
      <text class="address-label" x="675" y="1061">Postcode</text>
    </g>

    <polygon class="flap" points="184,609 812,609 824,673 184,673"/>
    <g transform="rotate(180 510 640)">
      <text class="flap-text" x="510" y="638">Go to rmzo-post.com.au to book your pickup.</text>
      <text class="flap-text" x="510" y="652">Carried subject to RM-ZO Standard Conditions of Carriage; see our website.</text>
    </g>
  </g>
</svg>
</body>
</html>
```